Course Graduation Certificate

This project is not for a flyer but instead for the creation of a course graduation certificate. The final certificate needs to include the Marlowe Summit Aviation Academy logo and the text stating as follows:
Certifies that ___________________________ has satisfactorily completed the course of _______________________________ on ________________________________
I would also like to include some type of gold seal of completion as well as a place to sign my name and credentials at the bottom of the certificate
I have included the Marlowe Summit Aviation Academy logo as well as three other certificate examples for you to work from.
Target Market(s)
Students completing a certification course and receiving a certificate
Look and feel

```html
<!DOCTYPE html>
<html lang="en">
<head>
<meta charset="utf-8">
<title>Course Graduation Certificate – Marlowe Summit Aviation Academy</title>
<link rel="stylesheet" href="https://fonts.googleapis.com/css2?family=Montserrat:wght@400;500;600&family=Poppins:ital,wght@1,800&display=swap">
<style>
  :root {
    --cobalt: #1a5fad;
    --cobalt-deep: #165aa6;
    --sky-line: #3b88d2;
    --sky-soft: #4d95d8;
    --paper: #ffffff;
    --stage: #ffffff;
    --ink: #2b2b2b;
    --rule: #6a6a6a;
    --gold: #d9a93a;
    --gold-light: #f2d57a;
    --ribbon: #c8262c;
  }
  * { box-sizing: border-box; margin: 0; padding: 0; }
  html, body { width: 1013px; height: 1200px; overflow: hidden; background: var(--stage); }
  body { position: relative; font-family: "Montserrat", sans-serif; color: var(--ink); }

  .certificate {
    position: absolute; left: 37px; top: 236px;
    width: 940px; height: 727px;
    background: var(--cobalt-deep);
  }
  .certificate__panel {
    position: absolute; left: 68px; top: 73px;
    width: 803px; height: 561px;
    background: var(--paper);
  }
  .certificate__frame {
    position: absolute; left: 12px; top: 12px; right: 12px; bottom: 12px;
    border: 5px solid var(--sky-line);
  }
  .certificate__flight-art {
    position: absolute;
    background: linear-gradient(160deg, var(--sky-soft), var(--sky-line));
    opacity: .85; border-radius: 6px;
  }
  .certificate__flight-art--left { left: 46px; top: 124px; width: 70px; height: 190px; }
  .certificate__flight-art--right { left: 830px; top: 460px; width: 62px; height: 166px; }

  .brand {
    position: absolute; left: 0; top: 104px; width: 940px;
    display: flex; justify-content: center; align-items: center; gap: 8px;
  }
  .brand__mark { width: 14px; height: 14px; background: var(--cobalt); }
  .brand__name { font-weight: 600; font-size: 20px; color: var(--cobalt); letter-spacing: .5px; }

  .certificate__title {
    position: absolute; left: 0; top: 168px; width: 940px;
    text-align: center;
    font-family: "Poppins", sans-serif; font-style: italic; font-weight: 800;
    font-size: 86px; line-height: 1; color: var(--cobalt); letter-spacing: 1px;
  }

  .field-label { position: absolute; font-size: 16px; line-height: 1; white-space: nowrap; }
  .field-rule { position: absolute; height: 1px; background: var(--rule); }

  .sign-rule { position: absolute; height: 1px; background: var(--rule); }
  .sign-label {
    position: absolute; font-size: 10px; text-transform: uppercase;
    text-align: center; letter-spacing: .3px;
  }

  .seal { position: absolute; left: 398px; top: 550px; width: 142px; height: 160px; }
</style>
</head>
<body>
  <main class="certificate">
    <div class="certificate__panel"><div class="certificate__frame"></div></div>

    <div class="certificate__flight-art certificate__flight-art--left" role="img" aria-label="Light blue jet silhouettes climbing along the left edge"></div>
    <div class="certificate__flight-art certificate__flight-art--right" role="img" aria-label="Light blue jet silhouettes climbing along the right edge"></div>

    <div class="brand">
      <span class="brand__mark"></span>
      <span class="brand__name">Marlowe Summit Aviation Academy</span>
    </div>

    <h1 class="certificate__title">CERTIFICATE</h1>

    <span class="field-label" style="left:206px; top:319px;">Certifies that</span>
    <span class="field-rule" style="left:320px; top:331px; width:491px;"></span>

    <span class="field-label" style="left:133px; top:353px;">has satisfactorily completed the course of</span>
    <span class="field-rule" style="left:478px; top:366px; width:333px;"></span>

    <span class="field-rule" style="left:131px; top:406px; width:306px;"></span>
    <span class="field-label" style="left:455px; top:399px;">on</span>
    <span class="field-rule" style="left:489px; top:406px; width:322px;"></span>

    <span class="sign-rule" style="left:188px; top:549px; width:132px;"></span>
    <span class="sign-label" style="left:188px; top:557px; width:132px;">Date</span>

    <span class="sign-rule" style="left:631px; top:549px; width:133px;"></span>
    <span class="sign-label" style="left:631px; top:561px; width:133px;">Signature</span>

    <svg class="seal" viewBox="0 0 142 160" role="img" aria-label="Gold seal of completion with red ribbons">
      <path d="M44 108 L30 152 L46 142 L56 156 L68 116 Z" fill="var(--ribbon)"/>
      <path d="M98 108 L112 152 L96 142 L86 156 L74 116 Z" fill="var(--ribbon)"/>
      <circle cx="71" cy="72" r="66" fill="var(--gold)"/>
      <circle cx="71" cy="72" r="54" fill="var(--gold-light)" opacity=".55"/>
    </svg>
  </main>
</body>
</html>
```